Personal creative Biz Card Design

Need personal yet natural and organic design. The cards I have now are well designed but look too commercial. I want more organic FEELING kind of card. I thought having a headshot would make it more personal... but maybe a sketch effect (or line drawing effect) of face better (?). Maybe in a gray or tungsten color?

Target Market(s)

Well, everyone i give card to will have already seen me face-to-face so that is one thing. Mostly yoga students and people interested in improving their fitness or general health. People looking for wellness, a personal fitness trainer, a yoga teacher

Industry/Entity Type

Health And Wellness

Contact Information for Business Card

I provided examples

Requirements
Must have
• My main logo
• My name

```html
<!DOCTYPE html>
<html lang="en">
<head>
<meta charset="utf-8">
<title>Owen Marlow – Business Card</title>
<link rel="stylesheet" href="https://fonts.googleapis.com/css2?family=Open+Sans:wght@400;600;700&display=swap">
<style>
  :root {
    --page-bg: #e4e4e4;
    --card-bg: #f4f4f2;
    --leaf-green: #3f8f2f;
    --swoosh-gray: #4a4a4a;
    --ink: #3a3a3a;
    --ink-soft: #6a6a6a;
    --white: #ffffff;
    --badge-navy: #2b3a7a;
    --badge-red: #c8283a;
    --badge-gray: #8a8a8a;
  }
  * { margin: 0; padding: 0; box-sizing: border-box; }
  html, body {
    width: 1105px; height: 1200px; overflow: hidden;
    background: var(--page-bg);
    font-family: "Open Sans", Arial, sans-serif;
    color: var(--ink);
  }
  .card {
    position: absolute; left: 112px;
    width: 880px; height: 506px;
    background: var(--card-bg);
    overflow: hidden;
  }
  .card--front { top: 60px; }
  .card--back { top: 634px; }

  /* Front */
  .front-swoosh { position: absolute; inset: 0; }
  .brand { position: absolute; left: 60px; top: 100px; display: flex; align-items: center; gap: 22px; }
  .brand__mark { width: 96px; height: 96px; border-radius: 50%; background: var(--leaf-green); }
  .brand__name {
    font-weight: 700; font-size: 52px; line-height: 1;
    color: var(--leaf-green); letter-spacing: 0.5px;
  }
  .brand__tagline {
    margin-top: 10px; font-weight: 400; font-size: 19px; color: var(--ink-soft);
  }
  .contact { position: absolute; right: 28px; top: 340px; list-style: none; }
  .contact__item {
    display: flex; justify-content: flex-end; align-items: center; gap: 14px;
    height: 35px; font-size: 22px; color: var(--white);
  }
  .contact__icon { width: 24px; height: 24px; flex: none; }

  /* Back */
  .services { position: absolute; left: 48px; top: 40px; list-style: none; }
  .services__item {
    position: relative; padding-left: 36px;
    font-size: 24px; line-height: 32px; margin-bottom: 5px; color: var(--ink);
  }
  .services__item--tall { margin-bottom: 12px; }
  .services__bullet { position: absolute; left: 0; top: 6px; width: 18px; height: 22px; }
  .portrait {
    position: absolute; left: 580px; top: 22px; width: 170px; height: 320px;
    background: linear-gradient(180deg, #bdbdbd 0%, #9a9a9a 55%, #e2e2e2 100%);
    border-radius: 70px 70px 8px 8px;
  }
  .divider { position: absolute; left: 46px; right: 42px; top: 344px; height: 2px; background: var(--leaf-green); }
  .badges { position: absolute; left: 38px; top: 392px; width: 831px; height: 72px; }
  .badge { position: absolute; }
  .badge--seal { left: 0; top: 0; width: 72px; height: 72px; border-radius: 50%; border: 4px solid var(--ink); background: var(--white); }
  .badge--council { left: 92px; top: 10px; width: 176px; height: 52px; background: var(--badge-navy); border-radius: 4px; }
  .badge--certified { left: 276px; top: 12px; width: 142px; height: 46px; background: var(--badge-red); border-radius: 4px; }
  .badge--academy { left: 421px; top: 16px; width: 208px; height: 38px; background: var(--badge-navy); border-radius: 4px; }
  .badge--studio { left: 635px; top: 0; width: 196px; height: 72px; background: var(--leaf-green); border-radius: 4px; opacity: 0.85; }
</style>
</head>
<body>

<section class="card card--front">
  <svg class="front-swoosh" viewBox="0 0 880 506" width="880" height="506" aria-hidden="true">
    <path d="M176,506 C420,410 700,250 880,30 L880,506 Z" fill="var(--leaf-green)"/>
    <path d="M150,506 C420,392 700,220 868,14 C710,240 440,410 188,506 Z" fill="var(--swoosh-gray)"/>
  </svg>

  <div class="brand">
    <span class="brand__mark"></span>
    <div>
      <div class="brand__name">OWEN MARLOW</div>
      <div class="brand__tagline">Expert Guidance for a Healthier Life</div>
    </div>
  </div>

  <ul class="contact">
    <li class="contact__item">555-014-2287
      <svg class="contact__icon" viewBox="0 0 24 24"><circle cx="12" cy="12" r="12" fill="var(--white)"/><path d="M8.2 6.5l2 2.2-1.1 1.6c.8 1.7 2 2.9 3.6 3.7l1.6-1.1 2.2 2-1 2c-4.6-.4-8.3-4.1-8.7-8.7z" fill="var(--leaf-green)"/></svg>
    </li>
    <li class="contact__item">owenstillpath@mail.com
      <svg class="contact__icon" viewBox="0 0 24 24"><circle cx="12" cy="12" r="12" fill="var(--white)"/><rect x="6" y="8" width="12" height="8.5" rx="1" fill="var(--leaf-green)"/><path d="M6.5 8.5L12 13l5.5-4.5" stroke="var(--white)" stroke-width="1.2" fill="none"/></svg>
    </li>
    <li class="contact__item">www.owenmarlow.com
      <svg class="contact__icon" viewBox="0 0 24 24"><circle cx="12" cy="12" r="12" fill="var(--white)"/><circle cx="12" cy="12" r="6" fill="none" stroke="var(--leaf-green)" stroke-width="1.6"/><path d="M6 12h12M12 6c-2.4 3.4-2.4 8.6 0 12M12 6c2.4 3.4 2.4 8.6 0 12" stroke="var(--leaf-green)" stroke-width="1.2" fill="none"/></svg>
    </li>
  </ul>
</section>

<section class="card card--back">
  <ul class="services">
    <li class="services__item"><svg class="services__bullet" viewBox="0 0 18 22"><path d="M9 2C3 6 3 14 9 20C15 14 15 6 9 2Z" fill="var(--leaf-green)"/></svg>Teacher of Yoga</li>
    <li class="services__item"><svg class="services__bullet" viewBox="0 0 18 22"><path d="M9 2C3 6 3 14 9 20C15 14 15 6 9 2Z" fill="var(--leaf-green)"/></svg>Leader of Yoga Teacher Trainings</li>
    <li class="services__item"><svg class="services__bullet" viewBox="0 0 18 22"><path d="M9 2C3 6 3 14 9 20C15 14 15 6 9 2Z" fill="var(--leaf-green)"/></svg>Personal Fitness Trainer</li>
    <li class="services__item"><svg class="services__bullet" viewBox="0 0 18 22"><path d="M9 2C3 6 3 14 9 20C15 14 15 6 9 2Z" fill="var(--leaf-green)"/></svg>Private &amp; public classes/sessions</li>
    <li class="services__item services__item--tall"><svg class="services__bullet" viewBox="0 0 18 22"><path d="M9 2C3 6 3 14 9 20C15 14 15 6 9 2Z" fill="var(--leaf-green)"/></svg>Nutrition, Wellness, Meditation,<br>Healing ceremonies (puja &amp; shamanic)</li>
    <li class="services__item"><svg class="services__bullet" viewBox="0 0 18 22"><path d="M9 2C3 6 3 14 9 20C15 14 15 6 9 2Z" fill="var(--leaf-green)"/></svg>Certified &amp; Insured</li>
  </ul>

  <div class="portrait" role="img" aria-label="Gray sketch-style headshot portrait of the trainer"></div>

  <div class="divider"></div>

  <div class="badges">
    <span class="badge badge--seal"></span>
    <span class="badge badge--council"></span>
    <span class="badge badge--certified"></span>
    <span class="badge badge--academy"></span>
    <span class="badge badge--studio"></span>
  </div>
</section>

</body>
</html>
```